design an app for runners to engage them in collective challenges

Creative Brief: Running Application - Collective Challenges
Objective
To design a simple yet impactful mobile application for runners, centered around collective challenges. The app should offer an engaging, user-friendly experience while encouraging participation in running challenges. Starting with a minimalist and robust version, the design must focus on essential features, allowing for future enhancements as the user base grows.

Target Audience
Primary Users: Casual to dedicated runners who enjoy tracking their progress and participating in challenges.
Motivations: Community-driven goals, personal achievements, and tangible rewards.
Needs: A visually appealing, straightforward interface with real-time progress tracking and clear challenge objectives.
Core Features
Main Screen: Current Challenge

Displays the active challenge with a title, visual, prize description, and countdown for kilometers remaining.
Prominent “Join” button for easy participation.
Quick access to challenge conditions (eg, most kilometers, fastest pace, random draw).
Challenge Details

Includes challenge rules, detailed prize information, and victory conditions.
Simplified text for clarity and engagement.
Past Challenges

Showcases previous challenges, total kilometers achieved, and winners.
Admin Section

Enables challenge creation with scheduling, descriptions, and victory criteria.
Minimalist design for ease of use.
Look and Feel
Visual Identity: Clean, modern, and energetic design reflecting the spirit of running and collective achievement.
Color Palette:
Vibrant primary colors: Blue and green for energy and motivation.
Accent colors: Orange or yellow for highlights, paired with a dark background for strong contrast.
Typography:
Sans-serif fonts like Lato or Montserrat for readability.
Bold, prominent numbers for key statistics like kilometers completed.
Icons and Graphics:
Minimalistic icons with light, functional animations (eg, a moving kilometer counter).
Clear, motivational visuals to support collective progress.
Tone and Style
Tone: Encouraging, community-focused, and goal-oriented.
Style: Minimalistic with a focus on clarity and user engagement.
References
Inspirations:
Velta Stride Circle for its simplicity and modern interface.
Quorvo for its community features and tracking precision.
Deliverables
Wireframes and UI designs for all key screens: login, current challenge, challenge details, past challenges, and admin panel.
Visual assets: icons, buttons, and animations.
A consistent design system to ensure scalability for future features.
Updates

Target Market(s)

Casual to dedicated runners who enjoy tracking their progress and participating in challenges.

Industry/Entity Type

sport

Font styles to use
Sans Serif

Colors

Designer to choose colors to be used in the design.

Requirements
Must have
• to design all screens

```html
<!DOCTYPE html>
<html lang="en">
<head>
<meta charset="utf-8">
<title>KMX Collective Challenges</title>
<link href="https://fonts.googleapis.com/css2?family=Roboto:wght@400;500;700;900&display=swap" rel="stylesheet">
<style>
:root{
  --bg:#0d0d0d;
  --screen:#000;
  --mint:#1fdc8f;
  --mint-text:#35f0a4;
  --sky:#29b6f6;
  --tile:#1c1c1c;
  --white:#fff;
  --ink:#111;
  --muted:#555;
}
*{box-sizing:border-box;margin:0;padding:0}
html,body{width:1200px;height:749px;overflow:hidden;background:var(--bg);font-family:'Roboto',sans-serif;color:var(--white)}
.screen{position:absolute;top:70px;width:262px;height:567px;background:var(--screen);border-radius:30px;overflow:hidden}
.s1{left:102px}.s2{left:465px}.s3{left:828px}
.abs{position:absolute}
.status{top:11px;left:19px;right:19px;display:flex;justify-content:space-between;font-size:8px;font-weight:500}
.status svg{display:block}
.brand{top:38px;left:0;right:0;text-align:center}
.brand-name{font-size:22px;font-weight:900;letter-spacing:8px;color:var(--mint-text);padding-left:8px;line-height:1}
.brand-sub{font-size:7.5px;font-weight:500;color:var(--sky);letter-spacing:-.1px;margin-top:3px}
.page-title{left:20px;top:92px;font-size:14px;font-weight:700}
.page-title.center{left:0;right:0;text-align:center;font-size:16px;top:98px}
.story{width:218px;height:108px;background:var(--white);display:flex;overflow:hidden}
.story-text{width:105px;padding:9px 0 0 12px;color:var(--ink)}
.story-text h3{font-size:10px;font-weight:500;line-height:14px}
.story-text p{font-size:7.4px;color:var(--muted);line-height:10.5px;margin-top:5px}
.story-text a{display:block;font-size:7.4px;color:var(--sky);margin-top:5px;text-decoration:underline}
.photo{flex:1;background:linear-gradient(180deg,#8fb3c9 0%,#b9cfdb 60%,#6d7d86 100%)}
.ring{left:26px;top:250px;width:94px;height:94px}
.ring-label{left:26px;top:280px;width:94px;text-align:center}
.ring-label b{display:block;font-size:16px;font-weight:700;line-height:16px}
.ring-label span{font-size:10px;font-weight:700}
.join{left:132px;top:281px;width:108px;height:29px;border-radius:15px;background:var(--mint);font-size:10px;font-weight:700;display:flex;align-items:center;justify-content:center}
.stat{width:67px;height:35px;background:var(--tile);border-radius:2px;text-align:center;padding-top:7px}
.stat b{display:block;font-size:8.5px;font-weight:700;color:var(--mint-text)}
.stat span{display:block;font-size:6.3px;font-weight:700;margin-top:2px}
.next{left:22px;top:405px;width:218px;height:108px;background:var(--sky);overflow:hidden}
.next-text{position:absolute;left:15px;top:13px;width:110px}
.next-text h3{font-size:10px;font-weight:700;line-height:14px}
.next-text p{font-size:7.4px;line-height:10.5px;margin-top:4px}
.next-text a{display:block;font-size:7.4px;color:var(--white);text-decoration:underline;margin-top:6px}
.next-photo{position:absolute;right:0;top:0;width:100px;height:108px;background:linear-gradient(160deg,#29b6f6 0%,#3a7aa8 60%,#2c4a62 100%)}
.nav{left:0;bottom:0;width:262px;height:46px;background:var(--mint);display:flex;justify-content:space-around;align-items:center;padding:0 14px}
.nav::before{content:"";position:absolute;top:0;left:122px;width:17px;height:2px;background:var(--white)}
.nav svg{width:16px;height:16px;fill:none;stroke:rgba(255,255,255,.55);stroke-width:2}
.nav .fill{fill:rgba(255,255,255,.55);stroke:none}
.nav .home{fill:var(--white);stroke:none}
.rules{left:20px;top:122px;list-style:none}
.rules li{display:flex;align-items:center;font-size:10px;height:21px}
.tick{width:9px;height:9px;margin:0 14px 0 4px;flex:none}
.prize{left:22px;width:219px;display:flex;gap:3px}
.prize div{height:24px;display:flex;align-items:center;justify-content:center;font-size:8.5px;width:48px;background:var(--tile)}
.prize .tag{width:63px;background:var(--sky);font-weight:700}
.prize .win{color:var(--mint-text)}
.prize .link{color:var(--sky);text-decoration:underline}
.victory{left:21px;top:328px;width:218px;height:176px;background:var(--sky);padding:13px 15px}
.victory h3{font-size:13px;font-weight:500;margin-bottom:6px}
.victory li{display:flex;font-size:9.5px;line-height:14px;margin-bottom:14px;list-style:none}
.victory li:nth-child(1){margin-bottom:7px}
.victory .tick{margin:2px 12px 0 1px}
.ongoing{left:20px;top:240px;width:221px;height:109px;background:var(--mint);text-align:center;padding-top:13px}
.ongoing h3{font-size:14px;font-weight:500}
.ongoing p{font-size:7.4px;line-height:10.5px;margin:5px auto 0;width:170px}
.chips{display:flex;justify-content:center;gap:6px;margin-top:8px}
.chips span{height:19px;background:var(--sky);font-size:7.4px;font-weight:700;text-decoration:underline;display:flex;align-items:center;justify-content:center}
.more{display:block;font-size:7.4px;font-weight:700;text-decoration:underline;margin-top:5px}
.trophy{left:55px;top:350px;width:143px;height:98px;background:radial-gradient(ellipse at 50% 45%,#c9922e 0%,#5a4120 35%,#1a1612 65%,#000 100%)}
</style>
</head>
<body>

<!-- Screen: current challenge -->
<section class="screen s1">
  <div class="abs status"><span>9:41</span><svg width="28" height="8" viewBox="0 0 28 8"><path d="M3 6l2-2 2 2-2 2z M1 3.5a6 6 0 0 1 8 0" fill="#fff" stroke="#fff" stroke-width=".8"/><rect x="17" y="1" width="9" height="6" rx="1" fill="none" stroke="#fff"/><rect x="18.5" y="2.5" width="6" height="3" fill="#fff"/></svg></div>
  <div class="abs brand"><div class="brand-name">KMX</div><div class="brand-sub">COLLECTIVE CHALLENGES</div></div>
  <h2 class="abs page-title center">THIS WEEK CHALLENGE</h2>
  <article class="abs story" style="left:22px;top:131px">
    <div class="story-text"><h3>Lorem ipsum dolor sit amet</h3><p>Lorem ipsum dolor sit amet, consectetur adi piscing elit, sed do eiusmod tempor</p><a>More Info</a></div>
    <div class="photo" role="img" aria-label="Two runners jogging outdoors under a pale sky"></div>
  </article>
  <svg class="abs ring" viewBox="0 0 94 94"><circle cx="47" cy="47" r="43" fill="none" stroke="#e6e6e6" stroke-width="6"/><circle cx="47" cy="47" r="43" fill="none" stroke="var(--sky)" stroke-width="7" stroke-dasharray="216 270" transform="rotate(-90 47 47)"/></svg>
  <div class="abs ring-label"><b>3</b><span>Kilometers</span></div>
  <div class="abs join">Join Challenge</div>
  <div class="abs stat" style="left:22px;top:358px"><b>03</b><span>Most Kilometers</span></div>
  <div class="abs stat" style="left:98px;top:358px"><b>05</b><span>Fastest Pace</span></div>
  <div class="abs stat" style="left:173px;top:358px"><b>02</b><span>Random Draw</span></div>
  <article class="abs next">
    <div class="next-photo" role="img" aria-label="Two runners sprinting mid-stride"></div>
    <div class="next-text"><h3>Next Week's Challenge</h3><p>Lorem ipsum dolor sit amet, consectetur adi piscing elit, sed do eiusmod tempor</p><a>&#9638; Jan 20,2024</a></div>
  </article>
  <nav class="abs nav">
    <svg viewBox="0 0 16 16"><circle cx="8" cy="5" r="3"/><path d="M2 15c0-4 3-5 6-5s6 1 6 5"/></svg>
    <svg viewBox="0 0 16 16"><path class="fill" d="M8 14L2 8a3.5 3.5 0 0 1 6-4 3.5 3.5 0 0 1 6 4z"/></svg>
    <svg viewBox="0 0 16 16"><path class="home" d="M8 1l7 6v8H1V7z"/></svg>
    <svg viewBox="0 0 16 16"><circle cx="8" cy="8" r="5" stroke-dasharray="2.5 1.4" stroke-width="3"/><circle cx="8" cy="8" r="2"/></svg>
    <svg viewBox="0 0 16 16"><circle cx="7" cy="7" r="5"/><path d="M11 11l4 4"/></svg>
  </nav>
</section>

<!-- Screen: challenge details -->
<section class="screen s2">
  <div class="abs status"><span>9:41</span><svg width="28" height="8" viewBox="0 0 28 8"><path d="M3 6l2-2 2 2-2 2z M1 3.5a6 6 0 0 1 8 0" fill="#fff" stroke="#fff" stroke-width=".8"/><rect x="17" y="1" width="9" height="6" rx="1" fill="none" stroke="#fff"/><rect x="18.5" y="2.5" width="6" height="3" fill="#fff"/></svg></div>
  <div class="abs brand"><div class="brand-name">KMX</div><div class="brand-sub">COLLECTIVE CHALLENGES</div></div>
  <h2 class="abs page-title">Challenge Rules</h2>
  <ul class="abs rules">
    <li><svg class="tick" viewBox="0 0 10 10"><circle cx="5" cy="5" r="5" fill="var(--mint)"/><path d="M2.8 5.2l1.5 1.5 3-3" stroke="#000" stroke-width="1.3" fill="none"/></svg>Lorem ipsum dolor sit amet, consectetur</li>
    <li><svg class="tick" viewBox="0 0 10 10"><circle cx="5" cy="5" r="5" fill="var(--mint)"/><path d="M2.8 5.2l1.5 1.5 3-3" stroke="#000" stroke-width="1.3" fill="none"/></svg>Adipiscing elit, sed do eiusmod tempor</li>
    <li><svg class="tick" viewBox="0 0 10 10"><circle cx="5" cy="5" r="5" fill="var(--mint)"/><path d="M2.8 5.2l1.5 1.5 3-3" stroke="#000" stroke-width="1.3" fill="none"/></svg>Incididunt ut labore et dolore magna aliqua</li>
    <li><svg class="tick" viewBox="0 0 10 10"><circle cx="5" cy="5" r="5" fill="var(--mint)"/><path d="M2.8 5.2l1.5 1.5 3-3" stroke="#000" stroke-width="1.3" fill="none"/></svg>Ut enim ad minim veniam, quis nostrud</li>
  </ul>
  <h2 class="abs page-title" style="top:225px">Prize Details</h2>
  <div class="abs prize" style="top:253px"><div class="tag">EASY RUN</div><div>25mins</div><div class="win">1st prize</div><div class="link">Details</div></div>
  <div class="abs prize" style="top:281px"><div class="tag">7MINS RUN</div><div>25mins</div><div class="win">1st prize</div><div class="link">Details</div></div>
  <div class="abs victory">
    <h3>Victory Conditions</h3>
    <ul>
      <li><svg class="tick" viewBox="0 0 10 10"><circle cx="5" cy="5" r="5" fill="#fff"/><path d="M2.8 5.2l1.5 1.5 3-3" stroke="var(--sky)" stroke-width="1.3" fill="none"/></svg>Lorem ipsum dolor sit amet,</li>
      <li><svg class="tick" viewBox="0 0 10 10"><circle cx="5" cy="5" r="5" fill="#fff"/><path d="M2.8 5.2l1.5 1.5 3-3" stroke="var(--sky)" stroke-width="1.3" fill="none"/></svg>Adipiscing elit, sed do eiusmod tempor</li>
      <li><svg class="tick" viewBox="0 0 10 10"><circle cx="5" cy="5" r="5" fill="#fff"/><path d="M2.8 5.2l1.5 1.5 3-3" stroke="var(--sky)" stroke-width="1.3" fill="none"/></svg>Incididunt ut labore et dolore magna aliqua</li>
      <li><svg class="tick" viewBox="0 0 10 10"><circle cx="5" cy="5" r="5" fill="#fff"/><path d="M2.8 5.2l1.5 1.5 3-3" stroke="var(--sky)" stroke-width="1.3" fill="none"/></svg>Ut enim ad minim veniam, quis</li>
    </ul>
  </div>
  <nav class="abs nav">
    <svg viewBox="0 0 16 16"><circle cx="8" cy="5" r="3"/><path d="M2 15c0-4 3-5 6-5s6 1 6 5"/></svg>
    <svg viewBox="0 0 16 16"><path class="fill" d="M8 14L2 8a3.5 3.5 0 0 1 6-4 3.5 3.5 0 0 1 6 4z"/></svg>
    <svg viewBox="0 0 16 16"><path class="home" d="M8 1l7 6v8H1V7z"/></svg>
    <svg viewBox="0 0 16 16"><circle cx="8" cy="8" r="5" stroke-dasharray="2.5 1.4" stroke-width="3"/><circle cx="8" cy="8" r="2"/></svg>
    <svg viewBox="0 0 16 16"><circle cx="7" cy="7" r="5"/><path d="M11 11l4 4"/></svg>
  </nav>
</section>

<!-- Screen: previous challenges -->
<section class="screen s3">
  <div class="abs status"><span>9:41</span><svg width="28" height="8" viewBox="0 0 28 8"><path d="M3 6l2-2 2 2-2 2z M1 3.5a6 6 0 0 1 8 0" fill="#fff" stroke="#fff" stroke-width=".8"/><rect x="17" y="1" width="9" height="6" rx="1" fill="none" stroke="#fff"/><rect x="18.5" y="2.5" width="6" height="3" fill="#fff"/></svg></div>
  <div class="abs brand"><div class="brand-name">KMX</div><div class="brand-sub">COLLECTIVE CHALLENGES</div></div>
  <h2 class="abs page-title">Previous Challenges</h2>
  <article class="abs story" style="left:21px;top:120px">
    <div class="story-text"><h3>Lorem ipsum dolor sit amet</h3><p>Lorem ipsum dolor sit amet, consectetur adi piscing elit, sed do eiusmod tempor</p><a>More Info</a></div>
    <div class="photo" role="img" aria-label="Two runners jogging outdoors under a pale sky"></div>
  </article>
  <div class="abs ongoing">
    <h3>Ongoing Challenge</h3>
    <p>Lorem ipsum dolor sit amet, consectetur adi piscing elit, sed do eiusmod tempor</p>
    <div class="chips"><span style="width:56px">20 Runners</span><span style="width:60px">7mins runs</span><span style="width:57px">1hour</span></div>
    <a class="more">More Info</a>
  </div>
  <div class="abs trophy" role="img" aria-label="Golden trophy cup glowing against a dark sparkling background"></div>
  <div class="abs stat" style="left:21px;top:458px"><b>03</b><span>Total Kilometers</span></div>
  <div class="abs stat" style="left:97px;top:458px"><b>50km</b><span>Average Speed</span></div>
  <div class="abs stat" style="left:173px;top:458px"><b>10</b><span>Fastest K.m</span></div>
  <nav class="abs nav">
    <svg viewBox="0 0 16 16"><circle cx="8" cy="5" r="3"/><path d="M2 15c0-4 3-5 6-5s6 1 6 5"/></svg>
    <svg viewBox="0 0 16 16"><path class="fill" d="M8 14L2 8a3.5 3.5 0 0 1 6-4 3.5 3.5 0 0 1 6 4z"/></svg>
    <svg viewBox="0 0 16 16"><path class="home" d="M8 1l7 6v8H1V7z"/></svg>
    <svg viewBox="0 0 16 16"><circle cx="8" cy="8" r="5" stroke-dasharray="2.5 1.4" stroke-width="3"/><circle cx="8" cy="8" r="2"/></svg>
    <svg viewBox="0 0 16 16"><circle cx="7" cy="7" r="5"/><path d="M11 11l4 4"/></svg>
  </nav>
</section>

</body>
</html>
```